Poem Handwritten by Veteran while in the jungle of Vietnam

My parents are celebrating their 50th wedding anniversary this year. I wanted to give them a very memorable gift. On my parents 2nd anniversary, my father was stationed in Vietnam. On that night he was in the jungle waiting till morning and wrote a poem to my mother using his pant leg as paper. I would like this poem to typographically designed to be framed and hung on the wall.

I have attached a picture of the poem below. It will need to be 11x14 when printed for framing. It would be great if there was background or artwork to make it more visually interesting, perhaps in a watercolor. My parents have a transitional style. I have attached some possible color schemes as well. Cool greens, blue, neutral grays, with hints of berries or highlights of yellow. These are just a guide, I would be open to your interpretations.

Thank you for your help. This will hopefully be a gift they will truly treasure as much as the poem itself.

Target Market(s)

My parents who are excited to be celebrating their 50th wedding anniversary. It should have a transitional, mature style.

Font styles to use
Serif
Script

Requirements
Must have
• The poem, typographically designed. There can be a mix of fonts, but legibility is critically important.
• Now that some designs have come through I wanted to give some more guidance of what I'm looking for. I want something that feels sophisticated and artistic.
Nice to have
• A background or art work, using the color schemes attached as a guide. I am really liking the designs that have a full color landscape artwork in the background. The fonts should be elegant and formal. I really like the romantic, muted colors. I had trouble finding similar projects online in the style I wanted until I cam across wedding invites. Those seem to be the most applicable. I've added pictures of some so you can get a sense of what I'm looking for. I am really liking the jungle foliage, starry skies or sunrises.
Should not have
• Cartoon caricatures, fonts that are too illegible when printed. I'm not liking anything whimsical. I don't like the very bright colors for this project.

```html
<!DOCTYPE html>
<html lang="en">
<head>
<meta charset="utf-8">
<title>Harold's Anniversary Poem</title>
<link rel="stylesheet" href="https://fonts.googleapis.com/css2?family=Cormorant+Garamond:wght@500;600;700&family=Open+Sans:wght@400&display=swap">
<style>
  :root {
    --page-bg: #e8e8e8;
    --sky-top: #a6cbe8;
    --sky-mid: #cfe0ec;
    --haze: #b7c2c7;
    --glow: #e2b676;
    --sun: #f6d58c;
    --hills: #5a5e55;
    --jungle: #2b2f28;
    --night: #0f1210;
    --heading: #3f4c60;
    --title: #2c3a52;
    --poem-ink: #1d2430;
    --note-ink: #7f8d9b;
    --rule: #6f7d90;
  }
  * { margin: 0; padding: 0; box-sizing: border-box; }
  html, body {
    width: 1200px;
    height: 1200px;
    overflow: hidden;
    background: var(--page-bg);
  }
  .poster {
    position: absolute;
    left: 150px;
    top: 27px;
    width: 900px;
    height: 1146px;
    overflow: hidden;
  }
  .landscape-art {
    position: absolute;
    inset: 0;
    background:
      radial-gradient(ellipse 260px 90px at 74% 64%, var(--sun) 0%, rgba(230,180,110,0.55) 45%, rgba(230,180,110,0) 100%),
      linear-gradient(180deg,
        var(--sky-top) 0%,
        var(--sky-mid) 30%,
        #c9d6dd 42%,
        var(--haze) 52%,
        #c8bca4 60%,
        var(--glow) 64%,
        #8a8674 68%,
        var(--hills) 72%,
        var(--jungle) 80%,
        var(--night) 100%);
  }
  .header {
    position: absolute;
    top: 50px;
    left: 0;
    width: 100%;
    text-align: center;
    font-family: "Cormorant Garamond", Georgia, serif;
  }
  .date-line {
    display: flex;
    align-items: center;
    justify-content: center;
    gap: 10px;
    padding: 0 16px;
    font-size: 25px;
    font-weight: 600;
    color: var(--heading);
    letter-spacing: 0.5px;
  }
  .date-line .rule {
    flex: 1;
    height: 1px;
    background: var(--rule);
    position: relative;
  }
  .date-line .rule::after {
    content: "";
    position: absolute;
    top: -3px;
    width: 7px;
    height: 7px;
    border-radius: 50%;
    background: var(--rule);
  }
  .date-line .rule.left::after { right: 0; }
  .date-line .rule.right::after { left: 0; }
  .title {
    font-size: 35px;
    font-weight: 700;
    color: var(--title);
    letter-spacing: 0.5px;
    line-height: 1.1;
    margin-top: 2px;
  }
  .poem {
    position: absolute;
    top: 150px;
    left: 0;
    width: 100%;
    font-family: "Open Sans", Arial, sans-serif;
    font-size: 14px;
    line-height: 18.8px;
    color: var(--poem-ink);
    text-align: center;
  }
  .poem-column {
    position: absolute;
    top: 0;
    width: 300px;
  }
  .poem-column.left { left: 136px; }
  .poem-column.right { left: 424px; }
  .stanza { margin-bottom: 18.8px; }
  .author-note {
    position: absolute;
    left: 66px;
    top: 997px;
    width: 776px;
    font-family: "Cormorant Garamond", Georgia, serif;
    font-size: 17.5px;
    font-weight: 500;
    line-height: 18.5px;
    color: var(--note-ink);
  }
</style>
</head>
<body>
  <main class="poster">
    <div class="landscape-art" role="img" aria-label="Watercolour landscape of a misty jungle valley at sunrise, pale blue sky fading to a golden glow over layered hills, with dark tree silhouettes and two birds in flight"></div>

    <header class="header">
      <div class="date-line">
        <span class="rule left"></span>
        <span>20 JULY 1970, MONDAY, LZ PROFESSIONAL</span>
        <span class="rule right"></span>
      </div>
      <h1 class="title">HAROLD’S ANNIVERSARY POEM</h1>
    </header>

    <section class="poem">
      <div class="poem-column left">
        <p class="stanza">Life’s journey began with a challenge,<br>It was heralded far and near.<br>The road led on forever,<br>Its completion was known to be dear.</p>
        <p class="stanza">From the garden of light it proceeded,<br>To the valley of shadows it led<br>Thorns and thistles adorned it,<br>Past abyss and crevice it sped.</p>
        <p class="stanza">The brave surged forward with courage,<br>The wise undaunted pressed on.<br>The mighty held high their banner,<br>We all awaited the dawn.</p>
        <p class="stanza">Though the pitfalls and hazards were many,<br>The pathway was clearly in view.<br>Straight and sure it glided,<br>Its course we knew to be true.</p>
        <p class="stanza">I knew you, Sweetheart, beforehand,<br>So precious and sweet were you.<br>Our moments of bliss were priceless,<br>Each day brought us joy anew.</p>
      </div>
      <div class="poem-column right">
        <p class="stanza">The call to progression beckoned,<br>At last I would have my chance<br>To clasp you to me forever,<br>And seal our divine romance.</p>
        <p class="stanza">I eagerly started the journey,<br>Though with sorrow, I left you behind.<br>With courage and faith I continued,<br>For I knew, that you later I’d find.</p>
        <p class="stanza">I diligently searched for you, Darling,<br>The roadway was both bleak and fair.<br>Though the years grew long in number,<br>I did not give up in despair.</p>
        <p class="stanza">At last in the distance I saw you,<br>So beautiful, lovely, and sweet !<br>Your attention I struggled to capture,<br>Your love I wrested to meet.</p>
        <p class="stanza">What rapture was mine in fulfillment,<br>As now together we stand.<br>To cherish and love each other,<br>While our plans and dreams expand.</p>
        <p class="stanza">I love you, Darling, forever,<br>My life you have made replete.<br>Our eternal mansion beckons,<br>Your love has made it complete.</p>
      </div>
    </section>

    <p class="author-note">This poem was written during the dark of night while on guard duty at L3 Professional in Viet Nam. I was at the time a 2 Lieutenant in the Infantry. The date was July 1970, our second anniversary. The orginal was penciled onto my fatique uniform, arranging only the key rthy-ming words without light to see</p>
  </main>
</body>
</html>
```